Business card design needed

Business Card design required for new small plumbing business.
Would like a logo/text look that is simple and unique and does not have to be representative of a plumbing company (ie. having a cartoon plumber or toilet etc) as the companyname is self explanatory.
Would like the main colour to be green (lime green).
Updates

Industry/Entity Type

Plumber

Contact Information for Business Card

BRAVELL PLUMBING
ABN 61 904 127 558 003

Trevor Hasketh
Licensed Plumber 83615
Phone: 0412 870 245

27 Bravell Drive,
Ferncombe. 3941 Westmere

Email: bravellplumbing@mailnest.example

Logo Text

Bravell Plumbing

Logo styles of interest
Character Logo
Wordmark Logo
Lettermark Logo

```html
<!DOCTYPE html>
<html lang="en">
<head>
<meta charset="utf-8">
<title>Bravell Plumbing – Business Card</title>
<link rel="stylesheet" href="https://fonts.googleapis.com/css2?family=Ubuntu:wght@400;500;700&display=swap">
<style>
  :root {
    --page: #dedad3;
    --card-light: #fbfbfb;
    --card-shade: #e4e4e4;
    --band: #555759;
    --band-text: #ffffff;
    --lime-dark: #1e7f26;
    --lime: #4dbb2e;
    --lime-light: #7fd84a;
    --name-light: #a5a7aa;
    --name-dark: #2f3133;
    --detail: #e8e8e8;
    --muted: #4a4c4e;
  }
  html, body {
    margin: 0;
    width: 1200px;
    height: 933px;
    overflow: hidden;
    background: var(--page);
    font-family: "Ubuntu", sans-serif;
  }
  .sheet {
    width: 1200px;
    height: 933px;
    display: flex;
    flex-direction: column;
    align-items: center;
    justify-content: center;
    gap: 40px;
  }
  .card {
    width: 720px;
    height: 400px;
    display: block;
    box-shadow: 0 10px 28px rgba(0,0,0,0.22);
  }
  .band { fill: var(--band); }
  .stripe { fill: var(--lime); }
  .headline {
    font-family: "Ubuntu", sans-serif;
    font-weight: 700;
    font-size: 30px;
    fill: var(--band-text);
    letter-spacing: 0.3px;
  }
  .detail {
    font-family: "Ubuntu", sans-serif;
    font-size: 13px;
    fill: var(--detail);
  }
  .bullet { fill: var(--lime-light); stroke: #ffffff; stroke-width: 1; }
  .name {
    font-family: "Ubuntu", sans-serif;
    font-size: 26px;
    font-weight: 700;
  }
  .name-first { fill: var(--name-light); }
  .name-last { fill: var(--name-dark); }
  .licence {
    font-family: "Ubuntu", sans-serif;
    font-size: 12.5px;
    fill: var(--muted);
  }
  .web {
    font-family: "Ubuntu", sans-serif;
    font-size: 13px;
    fill: var(--detail);
  }
</style>
</head>
<body>
<main class="sheet">

  <!-- Card front -->
  <svg class="card card-front" viewBox="0 0 720 400" xmlns="http://www.w3.org/2000/svg" aria-label="Bravell Plumbing business card, front">
    <defs>
      <linearGradient id="paper" x1="0" y1="0" x2="1" y2="1">
        <stop offset="0" stop-color="var(--card-light)"/>
        <stop offset="1" stop-color="var(--card-shade)"/>
      </linearGradient>
      <linearGradient id="lime-fold" x1="0" y1="0" x2="1" y2="1">
        <stop offset="0" stop-color="var(--lime-dark)"/>
        <stop offset="0.6" stop-color="var(--lime)"/>
        <stop offset="1" stop-color="var(--lime-light)"/>
      </linearGradient>
    </defs>
    <rect width="720" height="400" fill="url(#paper)"/>

    <polygon class="fold" points="350,0 450,0 432,92" fill="url(#lime-fold)"/>
    <polygon class="band" points="0,92 432,92 398,150 0,150"/>
    <polygon class="stripe" points="0,150 398,150 394,156 0,156"/>
    <text class="headline" x="30" y="132">BRAVELL PLUMBING ABN</text>

    <polygon class="band" points="398,166 720,166 720,268 380,268"/>
    <polygon class="fold" points="380,268 560,268 478,336" fill="url(#lime-fold)"/>
    <g class="contact">
      <circle class="bullet" cx="424" cy="184" r="4.5"/>
      <text class="detail" x="436" y="189">27 Bravell Drive, Ferncombe.</text>
      <text class="detail" x="436" y="206">3941 Westmere</text>
      <circle class="bullet" cx="424" cy="219" r="4.5"/>
      <text class="detail" x="436" y="224">61 904 127 558 003</text>
      <circle class="bullet" cx="424" cy="237" r="4.5"/>
      <text class="detail" x="436" y="242">0412 870 245</text>
      <circle class="bullet" cx="424" cy="255" r="4.5"/>
      <text class="detail" x="436" y="260">bravellplumbing@mailnest.example</text>
    </g>

    <text class="name" x="40" y="310"><tspan class="name-first">TREVOR </tspan><tspan class="name-last">Hasketh</tspan></text>
    <text class="licence" x="40" y="332">Licensed Plumber 83615</text>
  </svg>

  <!-- Card back -->
  <svg class="card card-back" viewBox="0 0 720 400" xmlns="http://www.w3.org/2000/svg" aria-label="Bravell Plumbing business card, back">
    <defs>
      <linearGradient id="paper-b" x1="0" y1="0" x2="1" y2="1">
        <stop offset="0" stop-color="var(--card-light)"/>
        <stop offset="1" stop-color="var(--card-shade)"/>
      </linearGradient>
      <linearGradient id="lime-fold-b" x1="0" y1="0" x2="1" y2="1">
        <stop offset="0" stop-color="var(--lime-dark)"/>
        <stop offset="0.6" stop-color="var(--lime)"/>
        <stop offset="1" stop-color="var(--lime-light)"/>
      </linearGradient>
    </defs>
    <rect width="720" height="400" fill="url(#paper-b)"/>

    <polygon class="fold" points="330,0 420,0 402,62" fill="url(#lime-fold-b)"/>
    <polygon class="band" points="420,0 720,0 720,44 406,44"/>
    <circle class="bullet" cx="436" cy="22" r="4.5"/>
    <text class="web" x="448" y="27">www.bravellplumbing.example</text>

    <polygon class="fold" points="560,212 712,212 650,140" fill="url(#lime-fold-b)"/>
    <polygon class="band" points="150,212 720,212 720,280 120,280"/>
    <polygon class="stripe" points="120,280 720,280 720,286 118,286"/>
    <text class="headline" x="170" y="257">BRAVELL PLUMBING ABN</text>
  </svg>

</main>
</body>
</html>
```